Advertising flyer for proofreading business.

Hello everyone,

I need an advertising flyer for a new proofreading company in Australia.

I would like your design in be in two sizes:
- A4 (to be posted on noticeboards),
- A6 (to be printed in larger quantity to give away)
(please see the size specification file attached).

The text file is attached (Ad Text) and it contains lots of information. Please feel free to include your choice of text from the text file, but please include Poster title, and highlight 'ESL' and students discounts.

I understand that it is impossible to include the same amount of information on A6 and A4, so please feel free to chose what fits on each of them, but please keep the design similar.

I have attached our company logo, but feel free to adjust it to the poster design (feel free to change the color as well). The original logo file contains circle around it, please feel free to remove it and include only the typeset as it can be seen here: http://www.lexmarka.com.au/.

Flyers will be printed, so please see the specification file for details.

I will do my best to respond to feedback as soon as possible.

I appreciate your participation, time and help,
Best wishes,
Bartosz

Target Market(s)

Students, authors

Industry/Entity Type

Business

Colors

Designer to choose colors to be used in the design.

Requirements
Must have
• It would be good if poster is easy to spot on busy noticeboards and attract attention.
• Please keep the poster in the positive/optimistic mood, and so that it focuses on students, maybe photos of graduates(?).
• Poster title,
• Please include the list of proof-read documents as they are described in the attached text file (Ad Text).
• Please highlight students discounts and ESL.
Nice to have
• I would like to leave the creative freedom to all designers so at this point I have not adjusted the Look and Feel sliders. Please feel free to offer your own take on this.
• It would be nice if most of the text could be fit to the poster.

```html
<!DOCTYPE html>
<html lang="en">
<head>
<meta charset="utf-8">
<title>Clearline – ESL Proofreading Flyers</title>
<link href="https://fonts.googleapis.com/css2?family=Source+Sans+3:ital,wght@0,400;0,600;0,700;1,400&family=Oswald:wght@500;600&display=swap" rel="stylesheet">
<style>
:root{
  --bg:#2d3033;
  --ink:#231f20;
  --teal:#2bb89a;
  --teal-light:#7fd3bf;
  --red:#e6202e;
  --red-dark:#5a0a10;
  --yellow:#fcc425;
  --blue:#00a6e0;
  --green:#72bd44;
  --purple:#c459a7;
  --white:#ffffff;
}
*{box-sizing:border-box;margin:0;padding:0}
html,body{width:1200px;height:1200px;overflow:hidden;background:var(--bg)}
body{font-family:"Source Sans 3",sans-serif;color:var(--ink);position:relative}
.flyer{position:absolute;width:682px;height:964px;background:var(--white);overflow:hidden;transform-origin:0 0}
.flyer--a4{left:54px;top:130px}
.flyer--a6{left:770px;top:613px;transform:scale(.5015)}
.flyer>*{position:absolute}
.hero{left:0;top:0;width:682px;height:480px}
.brand{left:0;width:682px;top:28px;text-align:center}
.brand-name{font-size:50px;font-weight:400;letter-spacing:-1px;line-height:1}
.brand-name::before{content:"";display:inline-block;width:13px;height:13px;border-radius:50%;background:var(--teal);margin-right:9px;vertical-align:middle}
.tagline{font-size:15px;margin-top:18px}
.price-badge{left:517px;top:18px;display:flex;align-items:center;gap:6px}
.price-badge .label{font-family:"Oswald",sans-serif;font-weight:600;color:var(--red);font-size:17px;line-height:17px;padding-right:6px;border-right:1.5px solid var(--red)}
.price-badge .amount{font-family:"Oswald",sans-serif;font-weight:600;color:var(--red);font-size:58px;line-height:1}
.price-badge .amount sup{font-size:26px;vertical-align:top;position:relative;top:2px}
.headline{left:17px;top:450px;font-weight:700;font-size:37px;line-height:38px}
.headline .accent{color:var(--teal)}
.pointer{left:213px;top:522px}
.intro{left:248px;top:490px;width:420px;font-size:17.5px;line-height:22px}
.intro p+p{margin-top:14px}
.doc-list{left:17px;top:650px;font-size:16px;line-height:21.9px}
.doc-list h3{color:var(--teal);font-size:17px;font-weight:700;margin-bottom:1px}
.doc-list li{list-style:none;padding-left:16px;position:relative}
.doc-list li::before{content:"✓";color:var(--teal);position:absolute;left:0}
.tile{width:136px;height:120px;color:var(--white);display:flex;flex-direction:column;justify-content:center;align-items:center;text-align:center;padding:6px 8px;font-size:15.5px;line-height:19.5px}
.tile .fold{position:absolute;right:0;top:0;width:16px;height:16px;background:linear-gradient(225deg,var(--white) 50%,rgba(0,0,0,.28) 50%)}
.tile b{font-weight:700}
.tile i{font-size:12.5px;line-height:16.5px}
.tile-teal{left:246px;top:631px;background:var(--teal)}
.tile-red{left:390px;top:631px;background:var(--red)}
.tile-red .dark{color:var(--red-dark)}
.tile-yellow{left:534px;top:631px;background:var(--yellow)}
.tile-yellow small{font-size:13px;line-height:16.5px;color:var(--ink)}
.tile-blue{left:246px;top:758px;background:var(--blue)}
.tile-green{left:390px;top:758px;background:var(--green)}
.tile-purple{left:534px;top:758px;height:176px;background:var(--purple);align-items:stretch;text-align:justify;justify-content:flex-start;padding:8px 7px;font-size:11.2px;line-height:13.8px}
.tile-purple .t-head{font-weight:700;font-size:13.5px;line-height:17px;text-align:left}
.tile-purple .t-name{font-weight:700;font-size:13.5px;line-height:16px;margin-top:2px;text-align:left}
.tile-purple .t-role{font-weight:700;color:var(--ink);font-size:11px;line-height:13.5px;text-align:left}
.contact{left:245px;top:888px;display:flex;align-items:flex-start;gap:8px}
.contact .cta{font-size:11.5px;line-height:15px;font-style:italic;margin-top:9px;white-space:nowrap}
.contact .cta b{color:var(--red);font-style:normal;font-weight:700}
.contact .phone{font-family:"Oswald",sans-serif;color:var(--red);font-size:27px;line-height:30px;font-weight:500;display:flex;align-items:center;gap:3px}
.contact .email{font-size:13px;font-weight:700;display:flex;align-items:center;gap:4px;white-space:nowrap}
.bottom-rule{left:0;bottom:0;width:682px;height:6px;background:var(--teal)}
</style>
</head>
<body>

<main class="flyer flyer--a4">
  <svg class="hero" viewBox="0 0 682 480" role="img" aria-label="Photo of smiling graduates in navy gowns throwing mortarboard caps into a bright sky">
    <defs>
      <linearGradient id="sky-a4" x1="0" y1="0" x2="0" y2="1">
        <stop offset="0" stop-color="#ffffff"/>
        <stop offset=".35" stop-color="#eef0f4"/>
        <stop offset=".65" stop-color="#5b6a8c"/>
        <stop offset="1" stop-color="#1f2a4a"/>
      </linearGradient>
    </defs>
    <path d="M0 0H682V380Q350 500 0 355Z" fill="url(#sky-a4)"/>
    <path d="M0 355Q350 500 682 380V398Q350 520 0 370Z" fill="var(--teal-light)"/>
    <path d="M0 370Q350 520 682 398V410Q350 532 0 382Z" fill="var(--teal)"/>
  </svg>
  <header class="brand">
    <div class="brand-name">Clearline</div>
    <p class="tagline">Professional, English Language Proofreading.</p>
  </header>
  <div class="price-badge">
    <div class="label">PRICES<br>START<br>@ ONLY</div>
    <div class="amount"><sup>$</sup>20</div>
  </div>
  <h1 class="headline">Help with<br><span class="accent">English as<br>a second<br>language</span><br>(ESL)</h1>
  <svg class="pointer" width="11" height="48" viewBox="0 0 11 48"><path d="M0 0L11 24L0 48Z" fill="var(--ink)"/></svg>
  <section class="intro">
    <p>Proofreading by a native English speaker with an English Honours degree.</p>
    <p>Includes correct all English language errors, spelling and grammar mistakes, reference checking and editing for style, coherence and clarity.</p>
  </section>
  <section class="doc-list">
    <h3>We will proofread your:</h3>
    <ul>
      <li>Essays &amp; Assignments</li>
      <li>Theses</li>
      <li>Resumes</li>
      <li>Business Correspondence</li>
      <li>Training Manuals</li>
      <li>Newsletters</li>
      <li>Advertising Copy</li>
      <li>Brochures, Catalogues &amp;<br>Media Releases</li>
      <li>Websites</li>
      <li>Presentations &amp; Speeches</li>
      <li>Novels &amp; Short Stories</li>
    </ul>
  </section>
  <div class="tile tile-teal"><span class="fold"></span><b>Prices start<br>at only $20</b><i>(short menus,<br>flyers, letters)</i></div>
  <div class="tile tile-red"><span class="fold"></span><b>Discounts <span class="dark">for</span><br><span class="dark">not-for-profit<br>organisations</span><br>and students</b></div>
  <div class="tile tile-yellow"><span class="fold"></span><b>Fast, negotiable<br>time-frames</b><small>(same day service<br>available by special<br>arrangement)</small></div>
  <div class="tile tile-blue"><span class="fold"></span><b>Package deals<br>on documents<br>over 50,000<br>words</b></div>
  <div class="tile tile-green"><span class="fold"></span><b>Great Student<br>Discount Rate:<br>$25 per hour</b><i>(roughly 1000 words<br>-4 pages - of well<br>-written text)</i></div>
  <div class="tile tile-purple"><span class="fold"></span>
    <span class="t-head">Testimonial:</span>
    <span>Hannah understood our requirements quickly and has been fantastic at delivering quality work, on time and within agreed budget. It's a pleasure to work with her.</span>
    <span class="t-name">Carol Mason</span>
    <span class="t-role">Operations Manager<br>northbayAU</span>
  </div>
  <section class="contact">
    <p class="cta"><b>Contact us</b> for an<br>obligation free quote:</p>
    <div>
      <div class="phone"><svg width="20" height="20" viewBox="0 0 24 24"><path d="M6.6 10.8c1.4 2.8 3.8 5.1 6.6 6.6l2.2-2.2c.3-.3.7-.4 1-.2 1.1.4 2.3.6 3.6.6.6 0 1 .4 1 1V20c0 .6-.4 1-1 1C10.6 21 3 13.4 3 4c0-.6.4-1 1-1h3.5c.6 0 1 .4 1 1 0 1.3.2 2.5.6 3.6.1.3 0 .7-.2 1z" fill="var(--ink)"/></svg>0400 123 456</div>
      <div class="email"><svg width="12" height="9" viewBox="0 0 14 11"><rect x=".75" y=".75" width="12.5" height="9.5" fill="none" stroke="var(--red)" stroke-width="1.5"/><path d="M1 1L7 6L13 1" fill="none" stroke="var(--red)" stroke-width="1.5"/></svg>hello@clearline.com.au</div>
    </div>
  </section>
  <div class="bottom-rule"></div>
</main>

<main class="flyer flyer--a6">
  <svg class="hero" viewBox="0 0 682 480" role="img" aria-label="Photo of smiling graduates in navy gowns throwing mortarboard caps into a bright sky">
    <defs>
      <linearGradient id="sky-a6" x1="0" y1="0" x2="0" y2="1">
        <stop offset="0" stop-color="#ffffff"/>
        <stop offset=".35" stop-color="#eef0f4"/>
        <stop offset=".65" stop-color="#5b6a8c"/>
        <stop offset="1" stop-color="#1f2a4a"/>
      </linearGradient>
    </defs>
    <path d="M0 0H682V380Q350 500 0 355Z" fill="url(#sky-a6)"/>
    <path d="M0 355Q350 500 682 380V398Q350 520 0 370Z" fill="var(--teal-light)"/>
    <path d="M0 370Q350 520 682 398V410Q350 532 0 382Z" fill="var(--teal)"/>
  </svg>
  <header class="brand">
    <div class="brand-name">Clearline</div>
    <p class="tagline">Professional, English Language Proofreading.</p>
  </header>
  <div class="price-badge">
    <div class="label">PRICES<br>START<br>@ ONLY</div>
    <div class="amount"><sup>$</sup>20</div>
  </div>
  <h1 class="headline">Help with<br><span class="accent">English as<br>a second<br>language</span><br>(ESL)</h1>
  <svg class="pointer" width="11" height="48" viewBox="0 0 11 48"><path d="M0 0L11 24L0 48Z" fill="var(--ink)"/></svg>
  <section class="intro">
    <p>Proofreading by a native English speaker with an English Honours degree.</p>
    <p>Includes correct all English language errors, spelling and grammar mistakes, reference checking and editing for style, coherence and clarity.</p>
  </section>
  <section class="doc-list">
    <h3>We will proofread your:</h3>
    <ul>
      <li>Essays &amp; Assignments</li>
      <li>Theses</li>
      <li>Resumes</li>
      <li>Business Correspondence</li>
      <li>Training Manuals</li>
      <li>Newsletters</li>
      <li>Advertising Copy</li>
      <li>Brochures, Catalogues &amp;<br>Media Releases</li>
      <li>Websites</li>
      <li>Presentations &amp; Speeches</li>
      <li>Novels &amp; Short Stories</li>
    </ul>
  </section>
  <div class="tile tile-teal"><span class="fold"></span><b>Prices start<br>at only $20</b><i>(short menus,<br>flyers, letters)</i></div>
  <div class="tile tile-red"><span class="fold"></span><b>Discounts <span class="dark">for</span><br><span class="dark">not-for-profit<br>organisations</span><br>and students</b></div>
  <div class="tile tile-yellow"><span class="fold"></span><b>Fast, negotiable<br>time-frames</b><small>(same day service<br>available by special<br>arrangement)</small></div>
  <div class="tile tile-blue"><span class="fold"></span><b>Package deals<br>on documents<br>over 50,000<br>words</b></div>
  <div class="tile tile-green"><span class="fold"></span><b>Great Student<br>Discount Rate:<br>$25 per hour</b><i>(roughly 1000 words<br>-4 pages - of well<br>-written text)</i></div>
  <div class="tile tile-purple"><span class="fold"></span>
    <span class="t-head">Testimonial:</span>
    <span>Hannah understood our requirements quickly and has been fantastic at delivering quality work, on time and within agreed budget. It's a pleasure to work with her.</span>
    <span class="t-name">Carol Mason</span>
    <span class="t-role">Operations Manager<br>northbayAU</span>
  </div>
  <section class="contact">
    <p class="cta"><b>Contact us</b> for an<br>obligation free quote:</p>
    <div>
      <div class="phone"><svg width="20" height="20" viewBox="0 0 24 24"><path d="M6.6 10.8c1.4 2.8 3.8 5.1 6.6 6.6l2.2-2.2c.3-.3.7-.4 1-.2 1.1.4 2.3.6 3.6.6.6 0 1 .4 1 1V20c0 .6-.4 1-1 1C10.6 21 3 13.4 3 4c0-.6.4-1 1-1h3.5c.6 0 1 .4 1 1 0 1.3.2 2.5.6 3.6.1.3 0 .7-.2 1z" fill="var(--ink)"/></svg>0400 123 456</div>
      <div class="email"><svg width="12" height="9" viewBox="0 0 14 11"><rect x=".75" y=".75" width="12.5" height="9.5" fill="none" stroke="var(--red)" stroke-width="1.5"/><path d="M1 1L7 6L13 1" fill="none" stroke="var(--red)" stroke-width="1.5"/></svg>hello@clearline.com.au</div>
    </div>
  </section>
  <div class="bottom-rule"></div>
</main>

</body>
</html>
```